Vela Norvina is a dietary supplement company and in need of label design for 4 products

label for 4 dietary supplement products :1- Biotin. Red bottle ( please see the picture attached, not the whole bottle is colored but rather its a white bottle with the upper part and lower part of the bottle colored)2- COQ10. Orange Bottle 3- Hair Skin Nail. Pink bottle 4- Probiotics. Green Bottle we like the label to:1- have a modern and sleek appearance with very limited graphics.2- have a transparent background( as the bottle is white )3- have the box with the supplement and ingredient to appear sideways( horizontal )4- to have a color matching the bottle color.attached you will find :1- the dimension of the bottle.2- four different labels for each of the products.3- two pictures of the bottles 4- picture of the caps5- Logo
Industry/Entity Type
Health And Wellness
Colors
Designer to choose colors to be used in the design.
Look and feel
Each slider illustrates characteristics of the customer's brand and the style your logo design should communicate.

```html
<!DOCTYPE html>
<html lang="en">
<head>
<meta charset="UTF-8">
<title>Vela Norvina Probiotics Label</title>
<link href="https://fonts.googleapis.com/css2?family=Arimo:wght@400;700&display=swap" rel="stylesheet">
<style>
  :root {
    --green: #3cb44a;
    --green-dark: #2e9e3c;
    --grey: #8a8c8f;
    --grey-dark: #6d6f72;
    --label: #ffffff;
    --backdrop: #ecebea;
  }
  * { margin: 0; padding: 0; box-sizing: border-box; }
  html, body {
    width: 1200px; height: 1200px; overflow: hidden;
    background: var(--backdrop);
    font-family: "Arimo", Arial, sans-serif;
  }
  .label {
    position: absolute; left: 280px; top: 40px;
    width: 640px; height: 1120px;
    background: var(--label);
    overflow: hidden;
  }
  .top-band { position: absolute; left: 0; top: 0; width: 640px; height: 120px; }
  .brand {
    position: absolute; left: 150px; top: 250px;
    display: flex; align-items: center; gap: 18px;
  }
  .brand-square { width: 26px; height: 26px; background: var(--green); }
  .brand-name { font-size: 44px; font-weight: 400; color: var(--grey-dark); letter-spacing: 1px; }
  .title { position: absolute; left: 96px; top: 400px; font-weight: 700; line-height: 0.9; }
  .title-pro { display: block; font-size: 170px; color: var(--grey); letter-spacing: -4px; }
  .title-biotics { display: block; font-size: 132px; color: var(--green); letter-spacing: -3px; }
  .potency {
    position: absolute; left: 100px; top: 710px;
    font-size: 60px; font-weight: 700; color: var(--grey-dark);
    padding-bottom: 8px; border-bottom: 3px solid var(--green);
    width: 390px;
  }
  .claim {
    position: absolute; left: 100px; top: 800px; width: 390px;
    font-size: 38px; line-height: 1.2; color: var(--green);
    padding-bottom: 8px; border-bottom: 3px solid var(--green);
  }
  .count {
    position: absolute; right: 62px; top: 845px; text-align: center;
    color: var(--grey-dark); font-weight: 700;
  }
  .count-number { display: block; font-size: 56px; line-height: 1; }
  .count-unit { display: block; font-size: 13px; letter-spacing: 1px; }
  .bottom-band { position: absolute; left: 0; bottom: 0; width: 640px; height: 170px; }
  .bottom-band text { font-family: "Arimo", Arial, sans-serif; }
</style>
</head>
<body>
  <div class="label">
    <svg class="top-band" viewBox="0 0 640 120" aria-hidden="true">
      <path d="M0 0 H640 V70 Q320 130 0 100 Z" fill="var(--green)"/>
    </svg>

    <div class="brand">
      <span class="brand-square"></span>
      <span class="brand-name">Vela Norvina</span>
    </div>

    <h1 class="title">
      <span class="title-pro">Pro</span>
      <span class="title-biotics">biotics</span>
    </h1>

    <p class="potency">40 Billion</p>
    <p class="claim">Supports Healthy<br>Skin, Nails &amp; Hair</p>

    <div class="count">
      <span class="count-number">90</span>
      <span class="count-unit">CAPSULES</span>
    </div>

    <svg class="bottom-band" viewBox="0 0 640 170" aria-hidden="true">
      <path d="M0 170 Q320 -40 640 170 Z" fill="var(--green)"/>
      <text x="320" y="128" text-anchor="middle" font-size="32" fill="#ffffff">Dietary Supplement</text>
    </svg>
  </div>
</body>
</html>
```